Booklet - I can pay more Urgent Project

Dear,
I need help to design a booklet for my startup, I have provided a booklet sample I want the same layout and organization. As you can see I'm not looking for a lot of colors or graphs, it should clean neat. The booklet size could be 8.5 x 11 or 8.5x5.5. This is urgent I need it in 24hr max.
My booklet content on word file named "Moss Lantern Booklet".
Booklet sample is on pdf file named "bookt_sample".
Nice cover design is helpful
Thank you.

Requirements
Must have
• Need to go to print by tomorrow - urgent project

```html
<!DOCTYPE html>
<html lang="en">
<head>
<meta charset="UTF-8">
<title>Team – Moss Lantern Booklet</title>
<link href="https://fonts.googleapis.com/css2?family=Jost:ital,wght@0,300;0,400;0,600;1,300&display=swap" rel="stylesheet">
<style>
  :root {
    --accent: #29abe2;
    --ink: #2b2b2b;
    --heading-ink: #4a4a4a;
    --footer-bg: #58585a;
    --footer-ink: #ffffff;
    --paper: #ffffff;
  }
  * { margin: 0; padding: 0; box-sizing: border-box; }
  html, body { width: 777px; height: 1200px; overflow: hidden; background: var(--paper); }
  body { font-family: "Jost", "Futura", sans-serif; color: var(--ink); }
  .page { position: relative; width: 777px; height: 1200px; overflow: hidden; }

  .section-tab { position: absolute; left: 70px; top: 0; width: 101px; height: 114px; }
  .section-title {
    position: absolute; left: 68px; top: 118px;
    font-weight: 300; font-size: 46px; line-height: 1; color: var(--ink); letter-spacing: 0.5px;
  }

  .member { position: absolute; left: 70px; width: 640px; }
  .member--first { top: 221px; }
  .member--second { top: 576px; }

  .portrait {
    position: absolute; left: 0; top: 0; width: 175px; height: 207px;
    border: 2px solid #fff; box-shadow: 0 1px 4px rgba(0,0,0,0.35);
  }
  .portrait--light { background: linear-gradient(180deg, #ececec 0%, #d8d2cc 55%, #2e3238 100%); }
  .portrait--dark { background: linear-gradient(180deg, #2e2a2a 0%, #5a4a44 50%, #7f95c4 100%); }

  .bio { position: absolute; left: 218px; top: 0; width: 420px; }
  .bio__name { font-weight: 600; font-size: 17px; line-height: 22px; color: var(--heading-ink); }
  .bio__role { font-style: italic; font-weight: 300; font-size: 17px; line-height: 22.4px; color: var(--accent); }
  .bio__text { font-weight: 300; font-size: 16.6px; line-height: 22.4px; color: var(--ink); }

  .footer {
    position: absolute; left: 0; bottom: 0; width: 777px; height: 54px;
    background: var(--footer-bg); color: var(--footer-ink);
  }
  .footer__page { position: absolute; left: 35px; top: 16px; font-weight: 600; font-size: 14px; }
  .footer__site { position: absolute; right: 36px; top: 15px; font-weight: 600; font-size: 15px; }
</style>
</head>
<body>
<div class="page">
  <svg class="section-tab" viewBox="0 0 101 114" aria-hidden="true">
    <polygon points="0,0 101,0 101,83 0,114" fill="var(--accent)"/>
  </svg>
  <h1 class="section-title">Team</h1>

  <section class="member member--first">
    <div class="portrait portrait--light" role="img" aria-label="Portrait photo of Idris Malouf"></div>
    <div class="bio">
      <h2 class="bio__name">Idris Malouf</h2>
      <p class="bio__role">Coder, Visual Designer, Document Technical Editor</p>
      <p class="bio__text">Idris chose the technology for the project, created the back end of the website, and coded most of the front end. In addition to writing the code for the website functionality, Idris handled the appearance for the site as a whole. He also created the visual design for both the poster and the booklet.</p>
    </div>
  </section>

  <section class="member member--second">
    <div class="portrait portrait--dark" role="img" aria-label="Portrait photo of Owen Halvorsen"></div>
    <div class="bio">
      <h2 class="bio__name">Owen Halvorsen</h2>
      <p class="bio__role">Artist, Site Architect, Writer</p>
      <p class="bio__text">Owen conceived and designed the overall website, creating the specifications for the features and planning the site layout. He handled most of the writing and provided the majority of the art used in the project.</p>
    </div>
  </section>

  <footer class="footer">
    <span class="footer__page">5</span>
    <span class="footer__site">MossLantern.net</span>
  </footer>
</div>
</body>
</html>
```